Brightstone Roofing Business Card

This is my current business card. But I’d like to make some changes. Somewhere on the card I’d like to list some of the services we offer. Maybe on the back? But I’d still like to keep the red. White and black modern look.

-residential & commercial roofing
-Roof Repairs & Maintenance
-Storm Damage & Insurance Claims specialist
-Christmas Lights and permanent Christmas lights
Fencing. Windows. Gutters. Siding. Sheetrock, painting.

```html
<!DOCTYPE html>
<html lang="en">
<head>
<meta charset="utf-8">
<title>Brightstone Roofing Business Card</title>
<link href="https://fonts.googleapis.com/css2?family=Oswald:wght@400;500;600;700&family=Montserrat:wght@400;500;700&display=swap" rel="stylesheet">
<style>
  :root {
    --red: #e61f26;
    --dark-red: #91181b;
    --black: #000000;
    --stripe: #262626;
    --white: #ffffff;
    --grey-text: #9a9a9a;
    --divider: #c8c8c8;
    --backdrop: #989898;
  }
  * { margin: 0; padding: 0; box-sizing: border-box; }
  html, body { width: 1200px; height: 1000px; overflow: hidden; }
  body { background: var(--backdrop); position: relative; font-family: "Oswald", sans-serif; }

  .card { position: absolute; width: 694px; height: 400px; border-radius: 26px; overflow: hidden; }
  .card-front { left: 248px; top: 72px; background: var(--white); }
  .card-back { left: 252px; top: 514px; }
  .card svg { position: absolute; left: 0; top: 0; display: block; }

  .brand { position: absolute; left: 48px; top: 70px; width: 280px; text-align: center; }
  .brand-mark { width: 134px; height: 134px; border-radius: 50%; background: var(--red); margin: 0 auto 16px; }
  .brand-name { font-family: "Oswald", sans-serif; font-weight: 700; color: var(--black); font-size: 30px; line-height: 34px; letter-spacing: 1px; text-transform: uppercase; }

  .divider { position: absolute; left: 352px; top: 40px; width: 2px; height: 260px; background: var(--divider); }

  .services { position: absolute; left: 377px; top: 36px; list-style: none; font-size: 18.5px; color: #1a1a1a; font-weight: 400; }
  .services li { height: 21.7px; line-height: 21.7px; white-space: nowrap; }
  .services .dot { color: var(--red); font-size: 13px; line-height: 0; margin-right: 4px; vertical-align: 2px; }
  .services .dot.inline { margin: 0 4px 0 5px; }

  .person { position: absolute; left: 383px; top: 206px; }
  .person-name { font-size: 24px; font-weight: 600; line-height: 30px; color: var(--black); }
  .person-name .first { color: var(--red); }
  .person-role { font-size: 20px; font-weight: 400; color: var(--grey-text); line-height: 24px; }

  .contact { position: absolute; left: 385px; top: 266px; list-style: none; font-family: "Montserrat", sans-serif; font-size: 14px; font-weight: 500; line-height: 18px; color: var(--black); }
  .contact li { display: flex; align-items: center; gap: 7px; }
  .contact svg { position: static; }

  .web-band { position: absolute; left: 0; top: 341px; width: 694px; height: 59px; }
  .web-address { position: absolute; left: 210px; top: 341px; line-height: 59px; font-family: "Montserrat", sans-serif; font-size: 23px; color: var(--white); letter-spacing: 0.5px; }
  .web-address b { font-weight: 700; }
</style>
</head>
<body>

<section class="card card-front">
  <div class="brand">
    <div class="brand-mark"></div>
    <div class="brand-name">Brightstone<br>Roofing Co.</div>
  </div>

  <div class="divider"></div>

  <ul class="services">
    <li><span class="dot">•</span>Residential &amp; Commercial Roofing</li>
    <li><span class="dot">•</span>Roof Repairs &amp; Maintenance</li>
    <li><span class="dot">•</span>Storm Damage &amp; Insurance Claims</li>
    <li><span class="dot">•</span>Specialist Christmas Lights and</li>
    <li><span class="dot">•</span>Permanent Christmas Lights</li>
    <li><span class="dot">•</span>Fencing<span class="dot inline">•</span>Windows<span class="dot inline">•</span>Gutters</li>
    <li><span class="dot">•</span>Siding<span class="dot inline">•</span>Sheetrock<span class="dot inline">•</span>Painting</li>
  </ul>

  <div class="person">
    <div class="person-name"><span class="first">DEAN</span> CARVER</div>
    <div class="person-role">OWNER</div>
  </div>

  <ul class="contact">
    <li>
      <svg width="13" height="13" viewBox="0 0 24 24" aria-hidden="true"><path fill="#e61f26" d="M6.6 10.8a15.1 15.1 0 0 0 6.6 6.6l2.2-2.2c.3-.3.7-.4 1-.2 1.1.4 2.3.6 3.6.6.6 0 1 .4 1 1V20c0 .6-.4 1-1 1A17 17 0 0 1 3 4c0-.6.4-1 1-1h3.5c.6 0 1 .4 1 1 0 1.3.2 2.5.6 3.6.1.3 0 .7-.2 1z"/></svg>
      682-555-0142
    </li>
    <li>
      <svg width="14" height="11" viewBox="0 0 24 18" aria-hidden="true"><rect x="0" y="0" width="24" height="18" fill="#e61f26"/><path d="M1 1l11 9 11-9" fill="none" stroke="#fff" stroke-width="2"/></svg>
      dean@brightstoneroofing.com
    </li>
  </ul>

  <svg class="web-band" width="694" height="59" viewBox="0 0 694 59" style="top:341px">
    <defs>
      <linearGradient id="band-pattern-fill" x1="0" y1="1" x2="1" y2="0">
        <stop offset="0" stop-color="#b81c20"/>
        <stop offset="1" stop-color="#e61f26"/>
      </linearGradient>
    </defs>
    <rect x="0" y="0" width="453" height="59" fill="var(--red)"/>
    <rect x="453" y="0" width="241" height="59" fill="var(--black)"/>
    <rect x="0" y="0" width="164" height="59" fill="url(#band-pattern-fill)" role="img" aria-label="Decorative diagonal stripe pattern area"/>
  </svg>
  <div class="web-address"><b>brightstoneroofing</b>.com</div>
</section>

<section class="card card-back">
  <svg width="694" height="400" viewBox="0 0 694 400">
    <defs>
      <linearGradient id="back-pattern-fill" x1="0" y1="0" x2="0" y2="1">
        <stop offset="0" stop-color="#7a1619"/>
        <stop offset="1" stop-color="#c81d23"/>
      </linearGradient>
    </defs>
    <rect x="0" y="0" width="467" height="123" fill="var(--dark-red)"/>
    <rect x="467" y="0" width="227" height="123" fill="var(--red)"/>
    <rect x="0" y="123" width="467" height="277" fill="var(--red)"/>
    <rect x="467" y="123" width="227" height="277" fill="var(--black)"/>
    <rect x="0" y="0" width="178" height="400" fill="url(#back-pattern-fill)" role="img" aria-label="Decorative diagonal stripe pattern area"/>
  </svg>
</section>

</body>
</html>
```